Disability Magazine – Cover + Full Inside Layout

About the Publication

Our magazine is a quarterly, high‑impact publication that celebrates the lives, achievements, and everyday experiences of people with disabilities. It aims to inform, inspire, and advocate for accessibility, inclusion, and empowerment across all communities.

Target Audience

Adults (18‑65) with visible or invisible disabilities
Caregivers, family members, and allies
Professionals in health, education, policy, and design fields
Advocates and NGOs focused on accessibility

Project Goals

Visually compelling cover that instantly signals the magazine’s inclusive mission.
Consistent, readable interior layout for feature articles, interviews, photo essays, and resource guides.
Design that works both in print (A4, 300 dpi) and digitally (PDF/online flipbook).

```html
<!DOCTYPE html>
<html lang="en">
<head>
<meta charset="utf-8">
<title>Disability Magazine – Cover and Inside Layout</title>
<link href="https://fonts.googleapis.com/css2?family=Playfair+Display:wght@400;700;900&family=Montserrat:wght@400;600;800&display=swap" rel="stylesheet">
<style>
:root{
  --bg:#e4e4e2;
  --navy:#1f2e44;
  --coral:#f0867c;
  --yellow:#f3b90f;
  --purple:#6c5fc8;
  --sky:#5aa7d9;
  --cream:#f4efe5;
  --ink:#1b1b1b;
  --white:#ffffff;
  --muted:#6f7480;
  --accent:#f2c33a;
}
*{box-sizing:border-box;margin:0;padding:0}
html,body{width:1200px;height:3108px;overflow:hidden}
body{background:var(--bg);font-family:"Montserrat",Arial,sans-serif;color:var(--ink);position:relative}

/* cover */
.cover{position:absolute;left:380px;top:60px;width:440px;height:600px;overflow:hidden;
  box-shadow:0 20px 40px rgba(0,0,0,.18)}
.cover-photo{position:absolute;inset:0;background:radial-gradient(ellipse at 50% 55%,#f1c5a6 0%,#d98a6c 35%,#7a8a4a 70%,#3d5a2e 100%)}
.masthead{font-family:"Montserrat",Arial,sans-serif;font-weight:800;color:var(--white);text-transform:uppercase;letter-spacing:2px;line-height:1}
.cover .masthead{position:absolute;top:26px;left:24px;font-size:54px}
.cover-sub{position:absolute;top:90px;left:26px;font-size:11px;letter-spacing:2px;color:var(--white);text-transform:uppercase}
.cover-lines{position:absolute;top:260px;right:20px;text-align:right;font-family:"Playfair Display",Georgia,serif;color:var(--accent);font-size:22px;font-weight:700;line-height:1.2}
.cover-lines small{display:block;margin-top:4px;font-family:"Montserrat",Arial,sans-serif;color:var(--white);font-size:10px;font-weight:400}

/* pages */
.page{position:absolute;width:188px;height:264px;overflow:hidden;background:var(--white);
  box-shadow:0 4px 10px rgba(0,0,0,.15)}
.ph{position:absolute;background:linear-gradient(135deg,#b9a38d,#6f6a5e)}
.ph.warm{background:linear-gradient(135deg,#e6b89b,#9a6b55)}
.ph.cool{background:linear-gradient(135deg,#a9bfcf,#5b6f80)}
.ph.sand{background:linear-gradient(180deg,#c9d7e0 0%,#d8b98f 55%,#a98462 100%)}
.ph.green{background:linear-gradient(135deg,#a8c48f,#5f7f4a)}
.ph.dark{background:linear-gradient(135deg,#6c6a66,#2e2d2b)}
.band{position:absolute;left:0;right:0}
.h{position:absolute;font-family:"Playfair Display",Georgia,serif;font-weight:700;line-height:1.1}
.hs{position:absolute;font-family:"Montserrat",Arial,sans-serif;font-weight:800;line-height:1.1;text-transform:uppercase}
.txt{position:absolute;font-size:5px;line-height:1.4;color:var(--muted)}
.tag{position:absolute;font-family:"Montserrat",Arial,sans-serif;font-weight:800;text-transform:uppercase;line-height:1.1;text-align:center}
</style>
</head>
<body>

<section class="cover" aria-label="Magazine cover">
  <div class="cover-photo" role="img" aria-label="Photo of a laughing child in a knitted hat"></div>
  <div class="masthead">Disability</div>
  <div class="cover-sub">Quarterly · Stories of inclusion</div>
  <div class="cover-lines">Every Voice<br>Counts<small>Stories of strength and access</small></div>
</section>

<!-- row 1 -->
<article class="page" style="left:52px;top:848px">
  <div class="ph warm" style="inset:0" role="img" aria-label="Cover photo of a laughing child"></div>
  <div class="masthead" style="position:absolute;top:12px;left:10px;font-size:18px">Disability</div>
</article>
<article class="page" style="left:280px;top:848px">
  <div class="ph warm" style="left:10px;top:12px;width:80px;height:90px" role="img" aria-label="Portrait photo"></div>
  <div class="ph cool" style="left:98px;top:12px;width:80px;height:44px" role="img" aria-label="Photo"></div>
  <div class="ph" style="left:98px;top:60px;width:80px;height:42px" role="img" aria-label="Photo"></div>
  <div class="band" style="top:120px;bottom:0;background:var(--navy)"></div>
  <div class="txt" style="top:132px;left:12px;right:12px;color:#c9d0db">A note from the editor on access and belonging.</div>
</article>
<article class="page" style="left:508px;top:848px">
  <div class="hs" style="top:12px;left:12px;font-size:9px">In this issue</div>
  <div class="txt" style="top:30px;left:12px;width:80px">04 Living fully<br>10 Public transport<br>18 Designed for people<br>26 Quiet work</div>
  <div class="ph cool" style="left:50px;top:120px;width:110px;height:120px" role="img" aria-label="Photo of a person in a wheelchair"></div>
</article>
<article class="page" style="left:736px;top:848px">
  <div class="band" style="top:0;height:120px;background:var(--coral)"></div>
  <div class="hs" style="top:30px;left:14px;font-size:15px;color:var(--white)">Living in a<br>World Not<br>Built for You</div>
  <div class="ph warm" style="left:0;right:0;top:120px;bottom:0" role="img" aria-label="Photo of a smiling woman"></div>
</article>
<article class="page" style="left:964px;top:848px">
  <div class="ph dark" style="inset:0" role="img" aria-label="Full page photo of a man"></div>
  <div class="hs" style="top:70px;left:78px;font-size:13px;color:var(--white)">Full page<br>poster ads</div>
</article>

<!-- row 2 -->
<article class="page" style="left:52px;top:1220px">
  <div class="hs" style="top:14px;left:10px;font-size:9px">A morning<br>that starts<br>differently</div>
  <div class="ph green" style="left:96px;top:10px;width:82px;height:110px" role="img" aria-label="Photo of prosthetic legs"></div>
  <div class="txt" style="top:60px;left:10px;width:80px">Routines shaped by care and patience.</div>
  <div class="band" style="top:200px;bottom:0;background:var(--navy)"></div>
</article>
<article class="page" style="left:280px;top:1220px">
  <div class="ph cool" style="left:8px;top:10px;width:80px;height:110px" role="img" aria-label="Photo"></div>
  <div class="h" style="top:14px;left:96px;width:84px;font-size:11px">When the world is not scaled for you</div>
  <div class="ph warm" style="left:8px;top:140px;width:172px;height:110px" role="img" aria-label="Photo of a family"></div>
</article>
<article class="page" style="left:508px;top:1220px">
  <div class="ph sand" style="inset:0" role="img" aria-label="Photo of a wheelchair user in the desert"></div>
  <div class="h" style="top:18px;left:0;right:0;text-align:center;font-size:13px;color:var(--navy)">Strength Without<br>Apology</div>
</article>
<article class="page" style="left:736px;top:1220px;background:var(--sky)">
  <div class="h" style="top:16px;left:12px;right:12px;font-size:11px;color:var(--white)">"Independence is built, not given"</div>
  <div class="ph warm" style="left:14px;top:110px;width:160px;height:100px" role="img" aria-label="Photo of a young woman"></div>
  <div class="txt" style="top:222px;left:14px;right:14px;color:var(--white)">Small wins make the biggest change.</div>
</article>
<article class="page" style="left:964px;top:1220px">
  <div class="band" style="top:0;height:150px;background:var(--sky)"></div>
  <div class="h" style="top:14px;left:12px;right:12px;font-size:11px;color:var(--white)">"Access means freedom"</div>
  <div class="ph warm" style="left:50px;top:60px;width:90px;height:150px" role="img" aria-label="Photo of a woman"></div>
  <div class="tag" style="left:12px;top:222px;width:164px;background:var(--coral);color:var(--white);font-size:8px;padding:5px">Full page poster ads</div>
</article>

<!-- row 3 -->
<article class="page" style="left:52px;top:1592px;background:var(--navy)">
  <div class="ph cool" style="left:10px;top:12px;width:168px;height:110px" role="img" aria-label="Photo of a person on crutches"></div>
  <div class="ph dark" style="left:10px;top:132px;width:168px;height:90px" role="img" aria-label="Photo"></div>
</article>
<article class="page" style="left:280px;top:1592px;background:var(--cream)">
  <div class="hs" style="top:16px;left:12px;font-size:11px;color:var(--coral)">When public<br>transport<br>becomes a<br>daily test</div>
  <div class="txt" style="top:82px;left:12px;width:90px">Ramps, lifts and timetables decide the day.</div>
  <div class="ph cool" style="left:92px;top:140px;width:86px;height:110px" role="img" aria-label="Photo at a bus stop"></div>
</article>
<article class="page" style="left:508px;top:1592px">
  <div class="h" style="top:14px;left:10px;width:84px;font-size:12px">Access is<br>a human right</div>
  <div class="ph warm" style="left:98px;top:10px;width:80px;height:100px" role="img" aria-label="Photo"></div>
  <div class="tag" style="left:0;right:0;top:150px;height:70px;background:var(--sky);color:var(--white);font-size:11px;padding-top:22px">Full page<br>poster ads</div>
</article>
<article class="page" style="left:736px;top:1592px">
  <div class="ph green" style="left:0;right:0;top:0;height:140px" role="img" aria-label="Photo outdoors in a park"></div>
  <div class="h" style="top:150px;left:12px;font-size:11px">Belonging in open spaces</div>
  <div class="txt" style="top:180px;left:12px;right:12px">Parks that welcome every visitor.</div>
</article>
<article class="page" style="left:964px;top:1592px">
  <div class="ph cool" style="left:60px;top:10px;width:118px;height:110px" role="img" aria-label="Photo of a wheelchair user"></div>
  <div class="txt" style="top:130px;left:12px;right:12px">Daily stories of quiet courage.</div>
  <div class="band" style="top:200px;bottom:0;background:var(--navy)"></div>
</article>

<!-- row 4 -->
<article class="page" style="left:52px;top:1960px;background:var(--yellow)">
  <div class="hs" style="top:18px;left:12px;font-size:16px;color:var(--white)">The<br>quiet<br>work</div>
  <div class="ph warm" style="left:96px;top:90px;width:82px;height:70px" role="img" aria-label="Photo of a caregiver"></div>
  <div class="ph cool" style="left:96px;top:170px;width:82px;height:80px" role="img" aria-label="Photo"></div>
</article>
<article class="page" style="left:280px;top:1960px">
  <div class="txt" style="top:14px;left:12px;width:76px">Support that nobody sees.</div>
  <div class="ph" style="left:96px;top:10px;width:82px;height:140px" role="img" aria-label="Photo of legs walking"></div>
  <div class="ph warm" style="left:12px;top:170px;width:90px;height:80px" role="img" aria-label="Photo"></div>
</article>
<article class="page" style="left:508px;top:1960px;background:var(--coral)">
  <div class="h" style="top:16px;left:12px;font-size:13px;color:var(--white)">Designed for<br>People, Not for<br>Trends</div>
  <div class="ph cool" style="left:12px;top:90px;width:164px;height:150px" role="img" aria-label="Photo of a woman seated"></div>
</article>
<article class="page" style="left:736px;top:1960px">
  <div class="hs" style="top:16px;left:12px;width:80px;font-size:10px">No one<br>builds<br>a life alone</div>
  <div class="ph warm" style="left:96px;top:10px;width:82px;height:90px" role="img" aria-label="Photo"></div>
  <div class="band" style="top:170px;height:40px;background:var(--coral)"></div>
  <div class="ph cool" style="left:12px;top:150px;width:70px;height:100px" role="img" aria-label="Photo"></div>
</article>
<article class="page" style="left:964px;top:1960px;background:var(--purple)">
  <div class="h" style="top:16px;left:0;right:0;text-align:center;font-size:12px;color:var(--white)">Where Survival<br>Turns into Strength</div>
  <div class="ph warm" style="left:14px;top:70px;width:160px;height:100px" role="img" aria-label="Photo"></div>
  <div class="tag" style="left:14px;top:190px;width:160px;color:var(--white);font-size:11px">Full page<br>poster ads</div>
</article>

<!-- row 5 -->
<article class="page" style="left:280px;top:2332px">
  <div class="hs" style="top:14px;left:12px;font-size:8px">Disability is not<br>a single story</div>
  <div class="ph warm" style="left:12px;top:50px;width:164px;height:90px" role="img" aria-label="Photo of two people"></div>
  <div class="ph cool" style="left:12px;top:150px;width:90px;height:100px" role="img" aria-label="Photo"></div>
  <div class="h" style="top:200px;left:110px;font-size:10px">Start Here</div>
</article>
<article class="page" style="left:508px;top:2332px;background:var(--navy)">
  <div class="h" style="top:16px;left:12px;font-size:12px;color:var(--white)">A Diverse<br>Community</div>
  <div class="ph warm" style="left:12px;top:70px;width:164px;height:90px" role="img" aria-label="Photo of a group"></div>
  <div class="ph cool" style="left:12px;top:170px;width:164px;height:80px" role="img" aria-label="Photo"></div>
</article>
<article class="page" style="left:736px;top:2332px">
  <div class="h" style="top:16px;left:12px;font-size:12px">A World<br>That Must<br>Learn Differently</div>
  <div class="ph cool" style="left:12px;top:100px;width:164px;height:150px" role="img" aria-label="Photo of a student"></div>
</article>

<!-- row 6 -->
<article class="page" style="left:280px;top:2700px;background:var(--coral)">
  <div class="h" style="top:16px;left:12px;font-size:12px;color:var(--white)">Voices that<br>Matter</div>
  <div class="ph warm" style="left:12px;top:70px;width:164px;height:80px" role="img" aria-label="Photo"></div>
  <div class="ph cool" style="left:12px;top:160px;width:164px;height:90px" role="img" aria-label="Photo"></div>
</article>
<article class="page" style="left:508px;top:2700px;background:var(--cream)">
  <div class="ph cool" style="left:12px;top:12px;width:164px;height:80px" role="img" aria-label="Photo"></div>
  <div class="tag" style="left:0;right:0;top:105px;font-size:18px;color:var(--navy)">Poster<br>Ads</div>
  <div class="ph warm" style="left:12px;top:160px;width:164px;height:90px" role="img" aria-label="Photo"></div>
</article>
<article class="page" style="left:736px;top:2700px;background:var(--ink)">
  <div class="h" style="top:14px;left:12px;right:12px;font-size:9px;color:var(--white)">Inclusion is Not Charity.<br>It is Justice.</div>
  <div class="ph warm" style="left:54px;top:70px;width:80px;height:110px" role="img" aria-label="Small cover of the magazine"></div>
  <div class="masthead" style="position:absolute;top:76px;left:54px;width:80px;text-align:center;font-size:8px;letter-spacing:1px">Disability</div>
  <div class="txt" style="top:200px;left:12px;right:12px;color:#bbb;text-align:center">Subscribe for four issues a year.</div>
</article>

</body>
</html>
```